A professional I.T consulting company requires a web design

Our company needs a fresh web design to help us drive our business forward. We are an Information Technology company who specialises in solutions based I.T delivery and consultations and who prides ourselves on our professional approach to business.

We would like a web site design from a designer who may be able to help us upload the site to WordPress and who may be interested in completing the "coding" section of the site (minimal coding). Although this is not essential to this project and won't factor into the decision making process.

A very thorough brief has been put together for this design project so very limited work is required in regards to content (the brief sets out all the content text - copy write material).

Please see the attached project documents for a copy of the brief

Target Market(s)

Please refer to the attached brief

Industry/Entity Type

Business

Requirements
Must have
• Please refer to the attached brief
Nice to have
Should not have

```html
<!DOCTYPE html>
<html lang="en">
<head>
<meta charset="utf-8">
<title>Korvit – IT Support and Solutions</title>
<link rel="stylesheet" href="https://fonts.googleapis.com/css2?family=Open+Sans:ital,wght@0,400;0,600;0,700;1,400&family=Source+Sans+3:wght@300;400;600;700&display=swap">
<style>
:root{
  --blue:#1e9fd8;
  --blue-dark:#1a7fc0;
  --nav-top:#48b6e8;
  --nav-bottom:#1d8ed1;
  --band-a:#3f8fd0;
  --band-b:#1e5ea6;
  --ink:#333b44;
  --text:#5a626b;
  --muted:#9aa1a8;
  --rule:#e6eaee;
  --panel:#eef3f6;
  --footer:#353a45;
  --footer-field:#474d59;
  --footer-base:#2b2f38;
  --white:#ffffff;
}
*{box-sizing:border-box;margin:0;padding:0}
html,body{width:1200px;height:2570px;overflow:hidden}
body{position:relative;background:var(--white);font-family:"Open Sans",Arial,sans-serif;color:var(--text);font-size:11px}
a{color:inherit;text-decoration:none}
ul{list-style:none}
.abs{position:absolute}
section,header,footer,nav{position:absolute;left:0;width:1200px}

/* header */
.site-header{top:0;height:76px;background:var(--white);border-top:2px solid #d8dde2}
.brand{position:absolute;left:160px;top:16px;display:flex;align-items:center;gap:8px}
.brand-dot{width:38px;height:38px;border-radius:50%;background:var(--blue)}
.brand-name{font-family:"Source Sans 3",sans-serif;font-weight:700;font-size:32px;color:var(--blue);letter-spacing:1px}
.header-links{position:absolute;top:18px;font-size:10.5px;line-height:20px;color:var(--muted)}
.header-links li{display:flex;align-items:center;gap:8px}
.header-links b{color:var(--ink);font-weight:600}
.mini-ico{width:11px;height:11px;background:var(--ink);border-radius:2px}

/* nav */
.main-nav{top:76px;height:38px;background:linear-gradient(var(--nav-top),var(--nav-bottom))}
.main-nav ul{position:absolute;left:160px;width:880px;height:38px;display:flex;justify-content:space-between;align-items:center;padding:0 12px}
.main-nav a{font-family:"Source Sans 3",sans-serif;font-weight:600;font-size:12.5px;color:var(--white);letter-spacing:.6px}

/* hero */
.hero{top:114px;height:354px;background:linear-gradient(115deg,#20395a 0%,#3f6d9c 30%,#a9c9e6 55%,#e9f2fa 65%,#7fa9d2 85%,#3e6a98 100%)}
.hero-card{position:absolute;left:162px;top:81px;width:426px;height:207px;background:rgba(22,28,36,.88);padding:30px 28px}
.hero-card h1{font-family:"Source Sans 3",sans-serif;font-weight:300;font-size:27px;color:var(--white);margin-bottom:12px}
.hero-card p{font-weight:700;font-size:12.5px;line-height:20px;color:var(--white)}
.btn{display:inline-block;background:var(--blue);color:var(--white);font-weight:600;font-size:11px;padding:0 16px;line-height:34px;border-radius:2px;margin-top:22px}
.hero-arrow{position:absolute;top:158px;width:46px;height:46px;background:rgba(40,46,56,.85);display:flex;align-items:center;justify-content:center}

/* clients */
.clients{top:468px;height:77px;background:linear-gradient(#f4f8fb,#dfe9f1)}
.clients ul{position:absolute;left:160px;width:880px;height:77px;display:flex}
.clients li{flex:1;display:flex;align-items:center;justify-content:center;border-left:1px solid #cfdbe5;font-family:"Source Sans 3",sans-serif;font-weight:600;font-size:15px;white-space:nowrap;color:#2a4b7a}
.clients li:last-child{border-right:1px solid #cfdbe5}

/* section titles */
.section-title{font-family:"Source Sans 3",sans-serif;font-weight:600;font-size:12.5px;letter-spacing:.4px;text-transform:uppercase;color:var(--ink)}
.section-title span{color:var(--blue)}
.read-more{display:flex;align-items:center;gap:8px;font-weight:600;font-size:10px;color:var(--ink)}
.read-more i{width:15px;height:15px;background:var(--blue);display:flex;align-items:center;justify-content:center}
.on-blue .read-more,.on-blue .section-title{color:var(--white)}
.on-blue .read-more i{background:#2aa6e0}

/* about */
.about{top:545px;height:300px}
.about-photo{position:absolute;left:160px;top:35px;width:205px;height:205px;border-radius:50%;background:radial-gradient(circle at 50% 40%,#c9b2a4,#8d96a3 60%,#dfe6ec)}
.about-body{position:absolute;left:387px;top:40px;width:413px}
.about-body p{font-size:9.8px;line-height:17px;margin-top:12px}
.about-body p b{color:var(--ink);font-weight:600}
.about-body .read-more{margin-top:12px}
.about-menu{position:absolute;left:838px;top:60px}
.about-menu li{display:flex;align-items:center;gap:13px;height:27px;font-size:9.8px;font-weight:600;color:var(--ink)}
.sq{width:15px;height:15px;background:var(--blue);display:flex;align-items:center;justify-content:center;flex:none}

/* why */
.why{top:845px;height:390px;background:linear-gradient(160deg,var(--band-a),#2f76bf 55%,var(--band-b))}
.why-photo{position:absolute;left:160px;top:70px;width:203px;height:108px;background:linear-gradient(135deg,#d7dde4,#8793a2)}
.why-intro{position:absolute;left:160px;top:193px;width:210px;font-size:9.8px;line-height:17px;color:var(--white)}
.feature{position:absolute;width:212px}
.feature .ico{position:absolute;left:0;top:0;width:48px;height:48px;border-radius:50%;background:var(--white);display:flex;align-items:center;justify-content:center}
.feature h3{margin-left:62px;font-family:"Source Sans 3",sans-serif;font-weight:400;font-size:17px;line-height:18px;color:var(--white)}
.feature p{margin:14px 0 0 62px;font-size:9.5px;line-height:16px;color:#e4efff}
.feature .bar{position:absolute;left:0;width:203px;height:6px;background:rgba(255,255,255,.14)}

/* services */
.services{top:1235px;height:395px}
.service{position:absolute;top:80px;width:203px}
.service .img{height:120px;background:linear-gradient(135deg,#e9edf1,#8e9aa8)}
.service h3{margin-top:20px;font-family:"Source Sans 3",sans-serif;font-weight:400;font-size:14.5px;color:var(--ink)}
.service p{margin-top:9px;font-size:9.5px;line-height:16px;color:var(--muted);height:52px}
.service .read-more{margin-top:10px}
.service .bar{margin-top:18px;height:6px;background:var(--rule)}

/* technologies */
.tech{top:1630px;height:320px;background:linear-gradient(160deg,var(--band-a),#2d74bd 50%,var(--band-b))}
.tech-photo{position:absolute;left:160px;top:72px;width:203px;height:105px;background:linear-gradient(135deg,#f2f5f8,#9eb1c6)}
.tech-intro{position:absolute;left:160px;top:190px;width:210px;font-size:9.5px;line-height:16px;color:var(--white)}
.tech-list{position:absolute;top:80px;font-size:9.5px;line-height:16px;color:var(--white)}
.tech-list li{margin-bottom:12px}
.tech-list b{font-weight:700}

/* testimonial */
.testimonial{top:1950px;height:205px}
.testimonial .intro{position:absolute;left:165px;top:55px;width:200px;font-size:9.8px;line-height:16px}
.testimonial .intro p{margin:12px 0 25px}
.client-photo{position:absolute;left:393px;top:40px;width:82px;height:82px;background:linear-gradient(160deg,#c8ccd1,#3c4654)}
.quote{position:absolute;left:490px;top:40px;width:550px;height:90px;background:var(--panel);padding:14px 18px;font-style:italic;font-size:9.8px;line-height:17px}
.cite{position:absolute;left:387px;top:143px;font-size:9.5px;color:var(--muted)}
.cite b{font-style:normal;font-weight:700;color:var(--ink);margin-right:10px}
.cite i{margin-left:10px}

/* footer */
.site-footer{top:2155px;height:375px;background:var(--footer);color:#a9afb8}
.f-title{position:absolute;font-family:"Source Sans 3",sans-serif;font-weight:600;font-size:12.5px;color:var(--white);letter-spacing:.4px;text-transform:uppercase}
.field{position:absolute;left:160px;width:352px;background:var(--footer-field);font-size:9.5px;color:#8d939c;padding:11px 14px}
.note{position:absolute;left:160px;top:318px;font-size:9.5px}
.send{position:absolute;left:408px;top:304px;width:104px;height:32px;background:var(--blue);color:var(--white);font-size:10.5px;font-weight:600;display:flex;align-items:center;justify-content:center;gap:6px}
.f-text{position:absolute;font-size:9.5px;line-height:16px}
.f-row{display:flex;gap:8px;align-items:flex-start;margin-bottom:12px}
.f-brand{position:absolute;left:835px;top:50px;display:flex;align-items:center;gap:8px}
.f-brand .brand-dot{width:46px;height:46px}
.f-brand .brand-name{font-size:38px}
.social{position:absolute;top:265px;left:835px;display:flex;gap:10px}
.social span{width:25px;height:25px;background:#4d535f;border-radius:2px}
.base{position:absolute;left:0;top:2530px;width:1200px;height:40px;background:var(--footer-base);font-size:8.5px;color:#6f7580}
.base .l{position:absolute;left:160px;top:15px}
.base .r{position:absolute;left:960px;top:15px}
</style>
</head>
<body>

<header class="site-header">
  <div class="brand"><span class="brand-dot"></span><span class="brand-name">KORVIT</span></div>
  <ul class="header-links" style="left:760px">
    <li><span class="mini-ico"></span>Live <b>Support</b></li>
    <li><span class="mini-ico"></span>Log <b>Service Call</b></li>
  </ul>
  <ul class="header-links" style="left:888px">
    <li><span class="mini-ico"></span>Call: <b>1800.555.0190</b></li>
    <li><span class="mini-ico"></span>Email: <b>info@korvit.com</b></li>
  </ul>
</header>

<nav class="main-nav">
  <ul>
    <li><a href="#">HOME</a></li>
    <li><a href="#">ABOUT US</a></li>
    <li><a href="#">WHY KORVIT</a></li>
    <li><a href="#">SERVICES SOLUTIONS</a></li>
    <li><a href="#">TECHNOLOGIES</a></li>
    <li><a href="#">CONTACT US</a></li>
  </ul>
</nav>

<section class="hero" role="img" aria-label="Hand touching a glowing digital interface with data and world map">
  <div class="hero-card">
    <h1>We succeed, when you succeed.</h1>
    <p>Our business is simple, provide you the best solutions and support possible to achive your goals.</p>
    <a class="btn" href="#">View Services</a>
  </div>
  <div class="hero-arrow" style="left:0"><svg width="12" height="16" viewBox="0 0 12 16"><path d="M9 2 3 8l6 6" fill="none" stroke="#fff" stroke-width="2"/></svg></div>
  <div class="hero-arrow" style="right:0"><svg width="12" height="16" viewBox="0 0 12 16"><path d="M3 2l6 6-6 6" fill="none" stroke="#fff" stroke-width="2"/></svg></div>
</section>

<section class="clients">
  <ul>
    <li>Corexa</li>
    <li>Halden Lawyers</li>
    <li>CareBridge Gippsland</li>
    <li>Voltara Energy</li>
    <li>Pipeline Pro</li>
    <li>Riverbend Health</li>
  </ul>
</section>

<section class="about">
  <div class="about-photo" role="img" aria-label="Portrait of the company director"></div>
  <div class="about-body">
    <h2 class="section-title">About <span>Korvit</span></h2>
    <p><b>Korvit is an Information Technology support and solution service provider founded and operating out of Gippsland in regional Victoria.</b> Korvit was established in May of 2013 and since that time, has been providing technical advisory and managed service solutions throughout Gippsland and the greater metropolitan areas.</p>
    <p>Our consultants are highly focused and committed to customer service and satisfaction and work hard to create lasting relationships with all we come into contact with. We pride ourselves on our personal investment into finding the right solution for our clients and in offering them a support network that is more akin to a personal relationship rather than a business partnership.</p>
    <a class="read-more" href="#">Read More <i><svg width="5" height="7" viewBox="0 0 5 7"><path d="M0 0l5 3.5L0 7z" fill="#fff"/></svg></i></a>
  </div>
  <ul class="about-menu">
    <li><span class="sq"><svg width="5" height="7" viewBox="0 0 5 7"><path d="M0 0l5 3.5L0 7z" fill="#fff"/></svg></span>Our History</li>
    <li><span class="sq"><svg width="5" height="7" viewBox="0 0 5 7"><path d="M0 0l5 3.5L0 7z" fill="#fff"/></svg></span>Us Now</li>
    <li><span class="sq"><svg width="5" height="7" viewBox="0 0 5 7"><path d="M0 0l5 3.5L0 7z" fill="#fff"/></svg></span>Our Team</li>
    <li><span class="sq"><svg width="5" height="7" viewBox="0 0 5 7"><path d="M0 0l5 3.5L0 7z" fill="#fff"/></svg></span>Our Clients</li>
    <li><span class="sq"><svg width="5" height="7" viewBox="0 0 5 7"><path d="M0 0l5 3.5L0 7z" fill="#fff"/></svg></span>Testimonials</li>
  </ul>
</section>

<section class="why on-blue">
  <h2 class="section-title abs" style="left:160px;top:50px">Why Korvit</h2>
  <div class="why-photo" role="img" aria-label="Team of consultants working together at a computer"></div>
  <p class="why-intro">In todays' modern business landscape, businesses must remain highly competitive and ensure that efficiency and performance are the top priorities. In short, your business needs to be better, faster and cheaper than ever before and must be on a path of continual improvement.</p>
  <a class="read-more abs" style="left:160px;top:340px" href="#">Read More <i><svg width="5" height="7" viewBox="0 0 5 7"><path d="M0 0l5 3.5L0 7z" fill="#fff"/></svg></i></a>

  <div class="feature" style="left:385px;top:42px">
    <span class="ico"><svg width="22" height="22" viewBox="0 0 22 22"><circle cx="9" cy="12" r="5" fill="none" stroke="#1e9fd8" stroke-width="3" stroke-dasharray="3 2"/><circle cx="9" cy="12" r="2" fill="#1e9fd8"/><circle cx="17" cy="5" r="3" fill="none" stroke="#1e9fd8" stroke-width="2"/></svg></span>
    <h3>We Customise<br>Our Solutions</h3>
    <p>Turpis tortor natoque a augue sociis habitasse enim, dis, elementum integer eu!</p>
    <span class="bar" style="top:141px"></span>
  </div>
  <div class="feature" style="left:610px;top:42px">
    <span class="ico"><svg width="24" height="20" viewBox="0 0 24 20"><circle cx="12" cy="6" r="4" fill="#1e9fd8"/><path d="M4 19c0-5 4-7 8-7s8 2 8 7z" fill="#1e9fd8"/><circle cx="4" cy="8" r="2.5" fill="#1e9fd8"/><circle cx="20" cy="8" r="2.5" fill="#1e9fd8"/></svg></span>
    <h3>Client Satisfaction<br>is Our Priority</h3>
    <p>Narra, auctor, in auctor! Purus phasellus velit mid, tristique aenean, eu non a integer.</p>
    <span class="bar" style="top:141px"></span>
  </div>
  <div class="feature" style="left:835px;top:42px">
    <span class="ico"><svg width="20" height="20" viewBox="0 0 20 20"><rect x="2" y="12" width="3" height="6" fill="#1e9fd8"/><rect x="7" y="8" width="3" height="10" fill="#1e9fd8"/><rect x="12" y="4" width="3" height="14" fill="#1e9fd8"/><rect x="17" y="1" width="2" height="17" fill="#1e9fd8"/></svg></span>
    <h3>Flexible<br>Pricing</h3>
    <p>Arcu, aenean. odio, magna sit nisi egestas duis cum egestas. Dictumst placerat.</p>
    <span class="bar" style="top:141px"></span>
  </div>
  <div class="feature" style="left:385px;top:215px">
    <span class="ico"><svg width="20" height="20" viewBox="0 0 20 20"><path d="M5 2h10v5a5 5 0 0 1-10 0z" fill="#1e9fd8"/><path d="M5 4H2v2a3 3 0 0 0 3 3M15 4h3v2a3 3 0 0 1-3 3" fill="none" stroke="#1e9fd8" stroke-width="1.5"/><rect x="9" y="12" width="2" height="4" fill="#1e9fd8"/><rect x="6" y="16" width="8" height="2" fill="#1e9fd8"/></svg></span>
    <h3>Our Solutions Work<br>and They Last</h3>
    <p>Turpis tortor natoque a augue sociis habitasse enim, dis, elementum integer eu!</p>
    <span class="bar" style="top:131px"></span>
  </div>
  <div class="feature" style="left:610px;top:215px">
    <span class="ico"><svg width="20" height="20" viewBox="0 0 20 20"><rect x="3" y="2" width="2" height="17" fill="#1e9fd8"/><path d="M5 3c4-2 6 2 11 0v8c-5 2-7-2-11 0z" fill="#1e9fd8"/></svg></span>
    <h3>We are Local<br>Company</h3>
    <p>Narra, auctor, in auctor! Purus phasellus velit mid, tristique aenean, eu non a integer.</p>
    <span class="bar" style="top:131px"></span>
  </div>
  <div class="feature" style="left:835px;top:215px">
    <span class="ico"><svg width="22" height="20" viewBox="0 0 22 20"><path d="M11 18 3 10a4.5 4.5 0 0 1 8-6 4.5 4.5 0 0 1 8 6z" fill="#1e9fd8"/></svg></span>
    <h3>We Love<br>Challenge</h3>
    <p>Arcu, aenean. odio, magna sit nisi egestas duis cum egestas. Dictumst placerat.</p>
    <span class="bar" style="top:131px"></span>
  </div>
</section>

<section class="services">
  <h2 class="section-title abs" style="left:160px;top:50px">Our <span>Services</span></h2>
  <article class="service" style="left:161px">
    <div class="img" role="img" aria-label="Support staff wearing headsets at computer desks"></div>
    <h3>Support Services</h3>
    <p>Ot porttitor mid elementum dictumst dignissim dapibus urna ac, enim? Porttitor! Aenean, urna, magna dictumst</p>
    <a class="read-more" href="#">Read More <i><svg width="5" height="7" viewBox="0 0 5 7"><path d="M0 0l5 3.5L0 7z" fill="#fff"/></svg></i></a>
    <div class="bar"></div>
  </article>
  <article class="service" style="left:386px">
    <div class="img" role="img" aria-label="Business handshake over a desk"></div>
    <h3>Managed Services</h3>
    <p>Ot porta montes montes vel nunc cras porttitor mid elementum dictumst dignissim dapibus urna ac, enim? Porttitor</p>
    <a class="read-more" href="#">Read More <i><svg width="5" height="7" viewBox="0 0 5 7"><path d="M0 0l5 3.5L0 7z" fill="#fff"/></svg></i></a>
    <div class="bar"></div>
  </article>
  <article class="service" style="left:611px">
    <div class="img" role="img" aria-label="Consultants reviewing a document together"></div>
    <h3>Consultancy Services</h3>
    <p>Ot urna, magna dictumst odio tincidunt rhoncus massa in in risus nunc augue phasellus mattis mid elementum dictumst</p>
    <a class="read-more" href="#">Read More <i><svg width="5" height="7" viewBox="0 0 5 7"><path d="M0 0l5 3.5L0 7z" fill="#fff"/></svg></i></a>
    <div class="bar"></div>
  </article>
  <article class="service" style="left:836px">
    <div class="img" role="img" aria-label="Hands typing on a laptop keyboard"></div>
    <h3>Hosted Services</h3>
    <p>Ot porttitor mid elementum dictumst dignissim urna ac, enim? Porttitor! Aenean, urna, magna dictumst odio, a tincidunt</p>
    <a class="read-more" href="#">Read More <i><svg width="5" height="7" viewBox="0 0 5 7"><path d="M0 0l5 3.5L0 7z" fill="#fff"/></svg></i></a>
    <div class="bar"></div>
  </article>
</section>

<section class="tech on-blue">
  <h2 class="section-title abs" style="left:160px;top:50px">Our Technologies</h2>
  <div class="tech-photo" role="img" aria-label="Hands working with charts and a keyboard"></div>
  <p class="tech-intro">Korvit engineers are highly skilled with experience in a diverse range of technologies. Our Engineers are certified in Vantrix, Corelane, and Hyperlyn technologies.</p>
  <ul class="tech-list" style="left:387px;width:260px">
    <li><b>Corelane:</b><br>Directory Hub, Mail Server, Data Server, Remote Desktop Services, &amp; Fleet Configuration Manager</li>
    <li><b>Remote:</b> Vantrix AppStream, EdgeGate, DeskStream 7, &amp; Hyperlyn Portal</li>
    <li><b>Thin Client:</b> Thinwell and Parallax</li>
    <li><b>Virtualisation:</b> Hyperlyn, Vantrix Host, and Corelane Hypervisor</li>
    <li><b>Backup and Disaster Recovery:</b> Rangeback, Vaultly, Shadowkeep, and Shieldline Backup</li>
  </ul>
  <ul class="tech-list" style="left:686px;width:354px">
    <li><b>Server Operating Systems:</b> Corelane Server 10, 11 and 12</li>
    <li><b>Server Operating Systems:</b> Corelane Desktop 5, 6, 7 and 8</li>
    <li><b>Server and Desktop Hardware:</b> Delvorn, Arvane and Parallax</li>
    <li><b>Shared Storage:</b> Arvane, Delvorn, Parallax, and Quelstor</li>
    <li><b>Intara:</b> Intara Pro and Intara Education Software</li>
  </ul>
  <a class="read-more abs" style="left:686px;top:260px" href="#">Read More <i><svg width="5" height="7" viewBox="0 0 5 7"><path d="M0 0l5 3.5L0 7z" fill="#fff"/></svg></i></a>
</section>

<section class="testimonial">
  <div class="intro">
    <h2 class="section-title">What our <span>client say</span></h2>
    <p>Let's hear what our clients think of our services.</p>
    <a class="read-more" href="#">More Testimonials <i><svg width="5" height="7" viewBox="0 0 5 7"><path d="M0 0l5 3.5L0 7z" fill="#fff"/></svg></i></a>
  </div>
  <div class="client-photo" role="img" aria-label="Portrait of a client in a suit"></div>
  <blockquote class="quote">"The staff at Korvit are the most enthusiastic and personable people I have met and have an extensive IT knowledge and thirst for greater knowledge. Our organisation has obtained a significant enhancement to our IT Network with the installation of a Vantrix environment in rapid time and Korvit has been able to pass on the knowledge and skills required for our people to operate this new environment."</blockquote>
  <p class="cite"><b>MARTIN HALLOWAY</b>|<i>Finance &amp; IT Manager / Company Secretary at Riverbend Community Health Service</i></p>
</section>

<footer class="site-footer">
  <h3 class="f-title" style="left:160px;top:48px">Contact Form</h3>
  <div class="field" style="top:78px;height:36px">Name</div>
  <div class="field" style="top:131px;height:36px">Email address</div>
  <div class="field" style="top:184px;height:108px">Massage</div>
  <p class="note">Email will never be published!</p>
  <a class="send" href="#">Send massage <svg width="10" height="8" viewBox="0 0 10 8"><path d="M1 4l3 3 5-6" fill="none" stroke="#fff" stroke-width="1.6"/></svg></a>

  <h3 class="f-title" style="left:610px;top:48px">Address</h3>
  <p class="f-text" style="left:610px;top:78px">42 Harbour Lane<br>Portside, VIC 3999<br>Australia</p>

  <h3 class="f-title" style="left:610px;top:158px">Contact</h3>
  <div class="f-text" style="left:610px;top:188px">
    <div class="f-row"><svg width="10" height="10" viewBox="0 0 10 10"><path d="M2 1l2 2-1 1.5a6 6 0 0 0 2.5 2.5L7 6l2 2-1.5 1.5C4 9 1 6 .5 2.5z" fill="#a9afb8"/></svg><span>+61 3 5550 1100<br>+61 3 5550 2100</span></div>
    <div class="f-row"><svg width="10" height="10" viewBox="0 0 10 10"><rect x=".5" y="2" width="9" height="6" fill="none" stroke="#a9afb8"/><path d="M.5 2l4.5 3.5L9.5 2" fill="none" stroke="#a9afb8"/></svg><span>support@example.com<br>info@example.com</span></div>
    <div class="f-row"><svg width="10" height="10" viewBox="0 0 10 10"><path d="M5 1 0 5h1.5v4h2.5V6.5h2V9h2.5V5H10z" fill="#a9afb8"/></svg><span>www.example.com</span></div>
  </div>

  <div class="f-brand"><span class="brand-dot"></span><span class="brand-name">KORVIT</span></div>

  <h3 class="f-title" style="left:835px;top:158px">Customer Service</h3>
  <p class="f-text" style="left:835px;top:188px">› Live Support<br>› Log Service Call<br>› Privacy and Security</p>

  <div class="social"><span></span><span></span><span></span></div>
</footer>

<div class="base">
  <span class="l">Copyright 2014 © Korvit - All Rights Reserved</span>
  <span class="r">Site Map &nbsp;|&nbsp; Privacy Policy</span>
</div>

</body>
</html>
```